Real Estate Agent needs business card design

We have logo designed already, want to have business card designed. Very interested in those smaller size business card as they look very trendy. Business name is called TOVANE REALTY

Industry/Entity Type

Business

```html
<!DOCTYPE html>
<html lang="en">
<head>
<meta charset="utf-8">
<title>Tovane Realty – Business Card</title>
<link href="https://fonts.googleapis.com/css2?family=Cinzel:wght@400;500&family=Roboto:wght@400&display=swap" rel="stylesheet">
<style>
  :root {
    --backdrop: #2b2b2b;
    --paper: #f3f3f2;
    --gold: #c49a66;
    --ink: #2d2d2d;
    --ink-soft: #4a4a4a;
    --rule: #9a9a9a;
    --charcoal: #2a2a2c;
    --white: #ffffff;
  }
  * { margin: 0; padding: 0; box-sizing: border-box; }
  html, body { width: 1200px; height: 960px; overflow: hidden; }
  body { background: var(--backdrop); position: relative; font-family: "Roboto", Arial, sans-serif; }

  .card { position: absolute; width: 600px; height: 343px; overflow: hidden; }
  .card-front { left: 302px; top: 129px; background: var(--paper); }
  .card-back { left: 299px; top: 488px; background: var(--gold); }

  .brand-name {
    position: absolute; right: 36px; top: 248px;
    font-family: "Cinzel", "Times New Roman", serif; font-weight: 500;
    font-size: 30px; color: var(--ink); letter-spacing: 0.5px; line-height: 1;
  }
  .brand-name { top: 120px; }

  .person { position: absolute; left: 37px; top: 189px; font-family: "Cinzel", "Times New Roman", serif; }
  .person-name { font-size: 22px; color: var(--gold); line-height: 1; letter-spacing: 0.5px; }
  .person-title { font-size: 14.5px; color: var(--ink); margin-top: 6px; letter-spacing: 0.4px; }

  .divider { position: absolute; left: 37px; right: 33px; top: 245px; height: 1px; background: var(--rule); }

  .contacts { position: absolute; top: 259px; left: 0; width: 600px; height: 40px; }
  .contact-group { position: absolute; top: 0; font-size: 14.5px; color: var(--ink-soft); line-height: 19px; }
  .contact-group.phones { left: 37px; }
  .contact-group.fax-mail { left: 187px; }
  .contact-group.address { left: 392px; }
  .contact-row { display: flex; align-items: center; white-space: nowrap; }
  .contact-row svg { width: 13px; height: 13px; margin-right: 9px; fill: var(--gold); flex: none; }
  .sep { position: absolute; top: 261px; width: 1px; height: 34px; background: var(--ink-soft); }
  .sep.one { left: 171px; }
  .sep.two { left: 376px; }

  .footer-band { position: absolute; left: 0; bottom: 0; width: 600px; height: 28px; }
  .footer-url {
    position: absolute; left: 37px; bottom: 7px;
    font-size: 13.5px; letter-spacing: 1.6px; color: var(--white);
  }

  .back-name {
    position: absolute; left: 507px; top: 36px;
    writing-mode: vertical-rl;
    font-family: "Cinzel", "Times New Roman", serif; font-weight: 500;
    font-size: 32px; color: var(--white); line-height: 1; letter-spacing: 0.5px;
  }
  .back-url {
    position: absolute; left: 486px; top: 40px;
    writing-mode: vertical-rl;
    font-size: 13px; letter-spacing: 6px; color: var(--white); line-height: 1;
  }
</style>
</head>
<body>

<section class="card card-front" aria-label="Business card front">
  <div class="brand-name">Tovane Realty</div>

  <div class="person">
    <div class="person-name">CLARA WESTON</div>
    <div class="person-title">CEO/FOUNDER</div>
  </div>

  <div class="divider"></div>

  <div class="contacts">
    <div class="contact-group phones">
      <div class="contact-row">
        <svg viewBox="0 0 24 24"><path d="M6.6 10.8a15.1 15.1 0 0 0 6.6 6.6l2.2-2.2a1 1 0 0 1 1-.25 11.4 11.4 0 0 0 3.6.57 1 1 0 0 1 1 1V20a1 1 0 0 1-1 1A17 17 0 0 1 3 4a1 1 0 0 1 1-1h3.5a1 1 0 0 1 1 1c0 1.25.2 2.45.57 3.6a1 1 0 0 1-.25 1z"/></svg>
        <span>555 214 7830</span>
      </div>
      <div class="contact-row">
        <svg viewBox="0 0 24 24"><path d="M7 1h10a2 2 0 0 1 2 2v18a2 2 0 0 1-2 2H7a2 2 0 0 1-2-2V3a2 2 0 0 1 2-2zm0 3v14h10V4zm5 15.5a1.2 1.2 0 1 0 0 2.4 1.2 1.2 0 0 0 0-2.4z"/></svg>
        <span>555 308 6194</span>
      </div>
    </div>

    <div class="contact-group fax-mail">
      <div class="contact-row">
        <svg viewBox="0 0 24 24"><path d="M6 2h12v5H6zM3 8h18a2 2 0 0 1 2 2v7h-4v5H5v-5H1v-7a2 2 0 0 1 2-2zm4 8v4h10v-4z"/></svg>
        <span>555 472 0318</span>
      </div>
      <div class="contact-row">
        <svg viewBox="0 0 24 24"><path d="M2 5h20v2l-10 6L2 7zm0 4.3 10 6 10-6V19H2z"/></svg>
        <span>hello@tovane.com</span>
      </div>
    </div>

    <div class="contact-group address">
      <div class="contact-row"><span>1420 Birchwood Court</span></div>
      <div class="contact-row"><span>Juniper Falls, Alaska 99801</span></div>
    </div>
  </div>
  <div class="sep one"></div>
  <div class="sep two"></div>

  <svg class="footer-band" viewBox="0 0 600 28" preserveAspectRatio="none" aria-hidden="true">
    <rect x="0" y="0" width="600" height="28" fill="var(--gold)"/>
    <polygon points="450,0 600,0 600,28 467,28" fill="var(--white)"/>
    <polygon points="455,0 600,0 600,28 472,28" fill="var(--charcoal)"/>
  </svg>
  <div class="footer-url">www.tovane.com</div>
</section>

<section class="card card-back" aria-label="Business card back">
  <div class="back-name">Tovane Realty</div>
  <div class="back-url">www.tovane.com</div>
</section>

</body>
</html>
```